Tallis Real Estate Yard Sign

Look to develop a real estate sign that would be place in the front yard or window of our clients. It will need to be able to be read from the road so the letter will need to be larger. The sign dimension will be 24" wide x 18" tell or 36" Wide x 24" Tall. We would like to use our house logo as the back part on the sign but we would like to see other creative options also. Our company name is Tallis Real Estate and our web address is Tallisrealestate.example. A spot for our phone number will also be required in the (XXX)-XXX-XXXX format. Please utilize our logo for the aesthetic feel of the sign.
Please include our company tagline. "Where Every Move Home Feels Simple and Easy"
This needs to be very eye catching and appealing to buyers. We want out Blue and Orange house to be very noticeable.
"Landscape format place
Target Market(s)
24-55 year olds.
Industry/Entity Type
Real Estate
Requirements
Must have
- Please be in Landscape. The sign is wider than it is tall.
It Needs to be eye catching and noticeable.

```html
<!DOCTYPE html>
<html lang="en">
<head>
<meta charset="utf-8">
<title>Tallis Real Estate Yard Sign</title>
<link href="https://fonts.googleapis.com/css2?family=Source+Sans+3:wght@400;600&family=Arimo&display=swap" rel="stylesheet">
<style>
  :root {
    --brand-blue: #0a55a3;
    --brand-orange: #f0821e;
    --sign-white: #ffffff;
    --backdrop: #d9d9d9;
    --label-ink: #111111;
  }
  html, body {
    margin: 0;
    padding: 0;
    width: 1200px;
    height: 900px;
    overflow: hidden;
    background: var(--backdrop);
  }
  .canvas {
    position: relative;
    width: 1200px;
    height: 900px;
  }
  .size-label {
    position: absolute;
    transform: translateX(-50%);
    font-family: "Arimo", sans-serif;
    font-size: 27px;
    color: var(--label-ink);
    white-space: nowrap;
    margin: 0;
  }
  .size-label--small { left: 283px; top: 144px; }
  .size-label--large { left: 848px; top: 226px; }

  .sign {
    position: absolute;
    background: var(--sign-white);
    overflow: hidden;
    font-family: "Source Sans 3", sans-serif;
  }
  .sign--small { left: 51px; top: 200px; width: 452px; height: 338px; }
  .sign--large { left: 559px; top: 278px; width: 579px; height: 462px; }

  .sign__band {
    position: absolute;
    inset: 0;
    width: 100%;
    height: 100%;
  }
  .band__swoosh { fill: none; stroke: var(--brand-orange); }
  .band__field { fill: var(--brand-blue); }

  .brand {
    position: absolute;
    display: flex;
    align-items: center;
    white-space: nowrap;
  }
  .brand__mark {
    background: var(--brand-orange);
    border-radius: 4px;
    flex: none;
  }
  .brand__name {
    color: var(--brand-blue);
    font-weight: 600;
    letter-spacing: -0.3px;
  }
  .sign--small .brand { left: 22px; top: 64px; gap: 12px; }
  .sign--small .brand__mark { width: 62px; height: 62px; }
  .sign--small .brand__name { font-size: 42px; }
  .sign--large .brand { left: 32px; top: 98px; gap: 14px; }
  .sign--large .brand__mark { width: 80px; height: 80px; }
  .sign--large .brand__name { font-size: 56px; }

  .tagline {
    position: absolute;
    left: 0;
    right: 0;
    text-align: center;
    margin: 0;
    color: var(--brand-orange);
    font-weight: 400;
    white-space: nowrap;
  }
  .sign--small .tagline { top: 159px; font-size: 20.5px; }
  .sign--large .tagline { top: 215px; font-size: 28px; }

  .contact {
    position: absolute;
    left: 0;
    right: 0;
    text-align: center;
    color: var(--sign-white);
    margin: 0;
    white-space: nowrap;
  }
  .contact__line { display: block; }
  .sign--small .contact { top: 254px; font-size: 22px; line-height: 30px; }
  .sign--large .contact { top: 332px; font-size: 33px; line-height: 45px; }
</style>
</head>
<body>
<main class="canvas">
  <p class="size-label size-label--small">18 in x 24 in</p>
  <p class="size-label size-label--large">24 in x 36in</p>

  <section class="sign sign--small" aria-label="Yard sign, 18 by 24 inches">
    <svg class="sign__band" viewBox="0 0 452 338" preserveAspectRatio="none" aria-hidden="true">
      <path class="band__swoosh" stroke-width="6" d="M0 256 Q226 200 452 240"/>
      <path class="band__field" d="M0 266 Q226 212 452 250 L452 338 L0 338 Z"/>
    </svg>
    <div class="brand">
      <span class="brand__mark"></span>
      <span class="brand__name">Tallis Real Estate</span>
    </div>
    <p class="tagline">Where Every Move Home Feels Simple and Easy</p>
    <p class="contact">
      <span class="contact__line">Tallisrealestate.example</span>
      <span class="contact__line">(XXX)-XXX-XXXX</span>
    </p>
  </section>

  <section class="sign sign--large" aria-label="Yard sign, 24 by 36 inches">
    <svg class="sign__band" viewBox="0 0 579 462" preserveAspectRatio="none" aria-hidden="true">
      <path class="band__swoosh" stroke-width="8" d="M0 336 Q290 266 579 326"/>
      <path class="band__field" d="M0 349 Q290 282 579 338 L579 462 L0 462 Z"/>
    </svg>
    <div class="brand">
      <span class="brand__mark"></span>
      <span class="brand__name">Tallis Real Estate</span>
    </div>
    <p class="tagline">Where Every Move Home Feels Simple and Easy</p>
    <p class="contact">
      <span class="contact__line">Tallisrealestate.example</span>
      <span class="contact__line">(XXX)-XXX-XXXX</span>
    </p>
  </section>
</main>
</body>
</html>
```